依頼詳細
依頼するページ
・トップページ
・コンセプトページ

清潔感があり、気軽に受講できる雰囲気を出しつつ、赤系を混ぜることで東北をITで盛り上げる熱意を伝えられるデザインを希望します。

提案頂いたデザインをもとに以下のページも作成していきます。
(継続依頼にするか、自社デザインにするかは検討中)
・講座の個別ページ
・開講中の講座一覧のページ
・問い合わせ
・東北地方のITについて紹介するページ(ブログ形式)

グローバルメニューを設置する想定でデザインをお願いします。
サイトURL
ページ数
2ページ
希望イメージ
シンプル 複雑
単色 カラフル
暗い 明るい
日常 高級
遊び心 厳粛
未来的 伝統的
女性的 男性的
希望する色
白、赤
納品ファイル
• イラストレーター形式 (.ai)
• PNG形式 (.png)
補足説明
お二人の方からご提案頂きました。
ありがとうございます。

お二人のご提案を拝見して追記させて頂きます。
コメントすることは大変恐縮なのですが、もう少し東北らしさや、東北を盛り上げることをアピールしたデザインでご提案頂ければと思います。

締め切りも3日ほど延ばさせて頂きました。

宜しくお願い致します。
皆様のご提案大変興味深く拝見しております。ありがとうございます。
社内で意見を集めた結果、もう少し提案を見てみたい、との意見が多く期限を延期する事と致しました。
修正がある方はこの機会にご提案頂けますと、大変嬉しく思います。
それでは宜しくお願い致します。
■ 選んだ理由

シンプルでありながら想いの伝わるデザインでした。

■ 提案者全員のお礼・コメント

みなさんのご提案一つ一つがとてもクオリティが高く、悩みました。ありがとうございました。

```html
<!DOCTYPE html>
<html lang="ja">
<head>
<meta charset="utf-8">
<title>みちのくITスクール</title>
<link href="https://fonts.googleapis.com/css2?family=Noto+Sans+JP:wght@400;500;700;900&display=swap" rel="stylesheet">
<style>
:root{
  --red:#d7000f;
  --red-dark:#b0000c;
  --ink:#333;
  --muted:#777;
  --line:#ddd;
  --page:#f2f2f2;
  --white:#fff;
  --green:#2e9e3c;
  --orange:#f08a00;
  --footer:#3a3a3a;
  --footer-text:#ccc;
}
*{box-sizing:border-box;margin:0;padding:0}
html,body{width:1200px;height:2171px;overflow:hidden}
body{font-family:"Noto Sans JP",sans-serif;color:var(--ink);background:var(--white);position:relative}
a{color:inherit;text-decoration:none}

.site-header{height:60px;display:flex;align-items:center;border-bottom:4px solid var(--red);background:var(--white)}
.brand{display:flex;align-items:baseline;gap:18px;padding-left:24px;width:680px}
.brand-name{font-size:28px;font-weight:700;color:var(--red)}
.brand-tagline{font-size:12px;color:var(--muted)}
.global-nav{display:flex;height:100%}
.global-nav a{display:flex;align-items:center;justify-content:center;font-size:15px;font-weight:500;border-left:1px solid var(--line);height:100%}
.global-nav a.current{background:var(--red);color:var(--white)}
.nav-home{width:140px}.nav-about{width:180px}.nav-courses{width:100px}.nav-blog{width:100px}

.hero{position:relative;height:460px;background:linear-gradient(180deg,#3d8fd6 0%,#8cc3ee 45%,#cfe6f5 62%,#5f8f4c 78%,#3f6f3a 100%)}
.hero-card{position:absolute;left:32px;top:90px;width:670px;height:230px;background:rgba(255,255,255,.95);padding:34px 36px}
.hero-title{font-size:40px;font-weight:900;color:var(--ink);letter-spacing:1px}
.hero-title em{font-style:normal;color:var(--red)}
.hero-title small{font-size:24px}
.hero-text{margin-top:22px;font-size:15px;line-height:1.9;color:var(--ink)}
.hero-cta{position:absolute;left:800px;top:210px;width:320px;height:60px;background:var(--red);color:var(--white);font-size:22px;font-weight:700;display:flex;align-items:center;justify-content:center;border-radius:4px;box-shadow:0 3px 0 var(--red-dark)}

.feature-banners{display:flex;justify-content:space-between;padding:16px 0 0;height:160px}
.feature{position:relative;height:130px;display:flex;flex-direction:column;align-items:center;justify-content:center;background:linear-gradient(180deg,#e9e9e9,#bdbdbd)}
.feature-about{width:790px}
.feature-blog{width:370px;background:linear-gradient(180deg,#f2f2f2,#cfcfcf)}
.feature-title{font-size:38px;font-weight:900;color:var(--ink);background:rgba(255,255,255,.8);padding:0 16px}
.feature-sub{font-size:14px;color:var(--ink);background:rgba(255,255,255,.8);padding:2px 12px;margin-top:6px}

.courses{background:var(--page);padding:20px 32px 30px;height:1120px}
.section-bar{display:flex;align-items:center;justify-content:center;position:relative;height:70px;background:var(--white);border:1px solid var(--line)}
.section-title{font-size:24px;font-weight:500;color:var(--ink)}
.section-bar .more-btn{position:absolute;right:20px;top:17px;background:var(--red);color:var(--white);font-size:14px;padding:8px 20px;border-radius:3px}
.course-grid{display:grid;grid-template-columns:repeat(3,356px);gap:24px 20px;margin-top:22px}
.course-card{background:var(--white);border:1px solid var(--line);padding:14px 16px 18px;height:466px}
.course-title{font-size:17px;font-weight:700;text-align:center}
.course-photo{position:relative;margin-top:12px;height:248px}
.photo-woman{background:linear-gradient(160deg,#f4f1ec,#d9cbb8 60%,#b89e86)}
.photo-laptop{background:linear-gradient(160deg,#fafafa,#e3e6ea 55%,#9aa3ad)}
.photo-stickers{background:linear-gradient(160deg,#3a4c8c,#8e2a3c 55%,#2b2f45)}
.status{position:absolute;left:8px;top:8px;color:var(--white);font-size:13px;font-weight:700;padding:3px 10px}
.status-open{background:var(--green)}
.status-soon{background:var(--orange)}
.course-meta{margin-top:14px;font-size:18px;line-height:1.6}
.course-btn{display:flex;align-items:center;justify-content:center;margin-top:12px;height:48px;background:var(--red);color:var(--white);font-size:16px;font-weight:700;border-radius:3px}
.all-link{display:block;text-align:right;margin-top:28px;color:var(--red);font-size:17px}

.site-footer{position:absolute;left:0;top:1800px;width:1200px;height:371px;background:var(--footer);color:var(--footer-text);padding:30px 32px}
.footer-cols{display:flex}
.footer-brand{width:520px}
.footer-logo{font-size:30px;font-weight:700;color:var(--red)}
.footer-label{display:flex;align-items:center;gap:8px;font-size:13px;margin-top:16px}
.footer-label::before{content:"";width:10px;height:10px;background:var(--red)}
.social-list{display:flex;gap:8px;margin-top:12px}
.social-list span{width:44px;height:44px;border-radius:4px;background:#5a5a5a}
.newsletter{display:flex;margin-top:12px}
.newsletter input{width:290px;height:36px;border:0;padding:0 10px;font-family:inherit;font-size:13px;color:var(--muted)}
.newsletter button{width:110px;height:36px;border:0;background:var(--red);color:var(--white);font-family:inherit;font-size:14px;margin-left:8px}
.footer-nav{width:320px;font-size:14px;line-height:1.9}
.footer-nav h3{font-size:15px;font-weight:500;color:var(--white)}
.copyright{position:absolute;bottom:24px;right:32px;font-size:13px}
</style>
</head>
<body>
<header class="site-header">
  <div class="brand"><span class="brand-name">みちのくITスクール</span><span class="brand-tagline">東北をITで元気にする</span></div>
  <nav class="global-nav">
    <a class="nav-home current" href="#">ホーム</a>
    <a class="nav-about" href="#">みちのくITスクールとは</a>
    <a class="nav-courses" href="#">講座一覧</a>
    <a class="nav-blog" href="#">みちのくITブログ</a>
  </nav>
</header>

<section class="hero" role="img" aria-label="青空と山並み、湖のある東北の風景写真">
  <div class="hero-card">
    <h1 class="hero-title"><em>東北</em><small>を元気にする</small><em>ITスクール</em><small>開講</small></h1>
    <p class="hero-text">サンプルテキストです。サンプルテキストです。サンプルテキストです。<br>サンプルテキストです。サンプルテキストです。サンプルテキストです。</p>
  </div>
  <a class="hero-cta" href="#">開講中の講座を探す</a>
</section>

<div class="feature-banners">
  <a class="feature feature-about" href="#" role="img" aria-label="街並みのモノクロ写真を背景にしたスクール紹介バナー">
    <span class="feature-title">みちのくITスクールとは</span>
    <span class="feature-sub">東北をITで盛り上げたい想いと取り組み</span>
  </a>
  <a class="feature feature-blog" href="#" role="img" aria-label="ノートパソコンの写真を背景にしたブログバナー">
    <span class="feature-title">みちのくITブログ</span>
    <span class="feature-sub">東北のITニュースやイベントを紹介</span>
  </a>
</div>

<main class="courses">
  <div class="section-bar">
    <h2 class="section-title">開講中の講座一覧</h2>
    <a class="more-btn" href="#">全ての講座を見る</a>
  </div>
  <div class="course-grid">
    <article class="course-card">
      <h3 class="course-title">趣味から始めるスマホアプリ作成</h3>
      <div class="course-photo photo-woman" role="img" aria-label="スマートフォンを持つ女性の写真"><span class="status status-open">開講中</span></div>
      <p class="course-meta">開催日：2013/12/31<br>定員20名 ¥20,000 6時間</p>
      <a class="course-btn" href="#">詳細を見る</a>
    </article>
    <article class="course-card">
      <h3 class="course-title">プログラミング入門</h3>
      <div class="course-photo photo-laptop" role="img" aria-label="ノートパソコンを使う女性の写真"><span class="status status-open">開講中</span></div>
      <p class="course-meta">開催日：2013/12/31<br>定員20名 ¥20,000 6時間</p>
      <a class="course-btn" href="#">詳細を見る</a>
    </article>
    <article class="course-card">
      <h3 class="course-title">CMS入門</h3>
      <div class="course-photo photo-stickers" role="img" aria-label="ステッカーが並ぶ机の写真"><span class="status status-soon">開講予定</span></div>
      <p class="course-meta">開催日：2013/12/31<br>定員20名 ¥20,000 6時間</p>
      <a class="course-btn" href="#">詳細を見る</a>
    </article>
    <article class="course-card">
      <h3 class="course-title">趣味から始めるスマホアプリ作成</h3>
      <div class="course-photo photo-woman" role="img" aria-label="スマートフォンを持つ女性の写真"><span class="status status-open">開講中</span></div>
      <p class="course-meta">開催日：2013/12/31<br>定員20名 ¥20,000 6時間</p>
      <a class="course-btn" href="#">詳細を見る</a>
    </article>
    <article class="course-card">
      <h3 class="course-title">プログラミング入門</h3>
      <div class="course-photo photo-laptop" role="img" aria-label="ノートパソコンを使う女性の写真"><span class="status status-open">開講中</span></div>
      <p class="course-meta">開催日：2013/12/31<br>定員20名 ¥20,000 6時間</p>
      <a class="course-btn" href="#">詳細を見る</a>
    </article>
    <article class="course-card">
      <h3 class="course-title">CMS入門</h3>
      <div class="course-photo photo-stickers" role="img" aria-label="ステッカーが並ぶ机の写真"><span class="status status-soon">開講予定</span></div>
      <p class="course-meta">開催日：2013/12/31<br>定員20名 ¥20,000 6時間</p>
      <a class="course-btn" href="#">詳細を見る</a>
    </article>
  </div>
  <a class="all-link" href="#">&gt;&gt;全ての講座を見る</a>
</main>

<footer class="site-footer">
  <div class="footer-cols">
    <div class="footer-brand">
      <div class="footer-logo">みちのくITスクール</div>
      <p class="footer-label">ソーシャルアカウント</p>
      <div class="social-list"><span></span><span></span><span></span><span></span><span></span><span></span></div>
      <p class="footer-label">メールマガジン登録 最新の講座情報をお届けします</p>
      <form class="newsletter"><input type="text" value="info@michinoku-it.jp" aria-label="メールアドレス"><button type="button">登録</button></form>
    </div>
    <nav class="footer-nav">
      <h3>講座</h3>
      <p>・講座を探す</p>
      <p>・全講座一覧</p>
      <p>・開講予定の講座</p>
      <p>・終了した講座</p>
    </nav>
    <nav class="footer-nav">
      <h3>スクール案内</h3>
      <p>・みちのくITスクールとは</p>
      <p>・講師紹介</p>
      <p>・よくある質問</p>
      <p>・お問い合わせ</p>
      <p>・みちのくITブログ</p>
    </nav>
  </div>
  <p class="copyright">Copyright (c) 2013 michinoku-it.jp All Rights Reserved.</p>
</footer>
</body>
</html>
```